Lumo Stack - Powerpoint Templates

We are a consultancy to help builders to optimize their planning in order to save building costs. For that reason we need templates for teasers and presentations where we offer our services, show our team and their capacities and present workflows, organization charts, price lists etc.

```html
<!DOCTYPE html>
<html lang="en">
<head>
<meta charset="utf-8">
<title>Lumo Stack – Presentation Templates</title>
<link href="https://fonts.googleapis.com/css2?family=Mulish:wght@400;600;700;800&display=swap" rel="stylesheet">
<style>
  :root {
    --page: #e6e7e9;
    --slide: #ffffff;
    --ink: #1e1e20;
    --heading: #38383b;
    --body: #4a4a4d;
    --panel: #3a3a3e;
    --panel-text: #e4e4e6;
    --gold: #b8822e;
    --gold-line: #c9a46a;
    --border: #c9c9cc;
    --grid: #e3e3e5;
    --green: #b5d334;
    --pink: #e4157f;
  }
  * { box-sizing: border-box; margin: 0; padding: 0; }
  html, body { width: 1200px; height: 3914px; overflow: hidden; }
  body { background: var(--page); font-family: "Mulish", Arial, sans-serif; color: var(--body); position: relative; }

  .slide { position: absolute; left: 99px; width: 1002px; height: 562px; background: var(--slide); overflow: hidden; }
  .slide--welcome { top: 106px; }
  .slide--services { top: 723px; }
  .slide--team { top: 1341px; }
  .slide--workflow { top: 1958px; }
  .slide--pricing { top: 2575px; }
  .slide--organization { top: 3191px; }

  .brand { position: absolute; left: 22px; top: 24px; display: flex; align-items: center; gap: 12px;
           font-weight: 800; font-size: 26px; letter-spacing: 2px; color: var(--heading); }
  .brand__square { width: 30px; height: 30px; background: var(--gold); }
  .slide-title { position: absolute; right: 22px; top: 38px; font-size: 26px; font-weight: 800; color: var(--heading); letter-spacing: .5px; }

  /* Welcome */
  .hero-photo { position: absolute; inset: 0;
    background: linear-gradient(115deg, #c7d6e6 0%, #a9c0d8 45%, #7f9cb8 70%, #4f6b86 100%); }
  .slide--welcome .brand { left: 87px; top: 110px; color: var(--ink); }
  .welcome-title { position: absolute; left: 87px; top: 205px; font-size: 58px; line-height: 70px; font-weight: 400; color: var(--ink); }

  /* Services */
  .services { position: absolute; left: 15px; top: 112px; display: flex; gap: 15px; }
  .service { width: 232px; height: 425px; background: var(--panel); color: var(--panel-text); text-align: center; padding: 30px 22px 0; }
  .service__icon { width: 70px; height: 70px; margin: 0 auto 12px; display: block; }
  .service__title { height: 48px; display: flex; align-items: flex-end; justify-content: center; font-size: 16px; line-height: 19px; font-weight: 400; color: #fff; margin-bottom: 10px; }
  .service__text { font-size: 12px; line-height: 15px; }

  /* Team */
  .team { position: absolute; left: 23px; top: 123px; display: flex; gap: 16px; }
  .member { width: 234px; height: 392px; border: 1px solid var(--border); }
  .member__photo { height: 193px; }
  .member__name { margin: 22px 21px 8px; font-size: 15px; font-weight: 800; color: var(--ink); }
  .member__text { margin: 0 21px; font-size: 12.5px; line-height: 15px; }

  /* Workflow */
  .timeline-line { position: absolute; left: 18px; right: 22px; top: 298px; height: 2px; background: var(--gold-line); }
  .step { position: absolute; width: 200px; margin-left: -100px; text-align: center; }
  .step__tick { position: absolute; left: 99px; width: 2px; background: var(--gold-line); }
  .step__title { font-size: 12px; font-weight: 800; color: var(--ink); margin-bottom: 9px; }
  .step__text { font-size: 12px; line-height: 15px; }
  .step--up { top: 104px; }
  .step--up .step__tick { top: 149px; height: 46px; }
  .step--down { top: 391px; }
  .step--down .step__tick { top: -91px; height: 68px; }

  /* Pricing */
  .plans { position: absolute; left: 24px; top: 120px; display: flex; gap: 22px; }
  .plan { width: 301px; height: 412px; border: 1px solid var(--border); }
  .plan__head { height: 112px; background: var(--gold); color: #fff; text-align: center; padding-top: 24px; }
  .plan__name { font-size: 20px; font-weight: 600; }
  .plan__price { font-size: 25px; font-weight: 400; margin-top: 4px; }
  .plan__list { list-style: none; padding: 18px 0 0 22px; }
  .plan__list li { font-size: 12px; line-height: 25px; position: relative; padding-left: 14px; }
  .plan__list li::before { content: ""; position: absolute; left: 0; top: 9px; border-left: 5px solid var(--gold); border-top: 4px solid transparent; border-bottom: 4px solid transparent; }

  /* Organization */
  .org-heading { position: absolute; left: 0; right: 0; top: 108px; text-align: center; font-size: 19px; font-weight: 800; color: var(--heading); }
  .org-sub { position: absolute; left: 0; right: 0; top: 137px; text-align: center; font-size: 18px; color: var(--ink); }
  .chart { position: absolute; left: 0; top: 0; }
  .chart text { font-family: "Mulish", Arial, sans-serif; font-size: 9px; fill: #555; }
</style>
</head>
<body>

<section class="slide slide--welcome">
  <div class="hero-photo" role="img" aria-label="Photo of a curved glass office tower against a cloudy blue sky"></div>
  <div class="brand"><span class="brand__square"></span>LUMO STACK</div>
  <h1 class="welcome-title">WELCOME TO<br>LUMO STACK</h1>
</section>

<section class="slide slide--services">
  <div class="brand"><span class="brand__square"></span>LUMO STACK</div>
  <h2 class="slide-title">OUR SERVICES</h2>
  <div class="services">
    <article class="service">
      <svg class="service__icon" viewBox="0 0 70 70" fill="none" stroke="#b8822e" stroke-width="2.5"><circle cx="32" cy="33" r="22"/><text x="32" y="42" text-anchor="middle" font-size="26" font-weight="700" fill="#b8822e" stroke="none" font-family="Mulish, sans-serif">$</text><path d="M52 40v16M46 50l6 6 6-6"/></svg>
      <h3 class="service__title">COST OPTIMIZATION CONSULTANCY</h3>
      <p class="service__text">Lorem ipsum dolor sit amet, consectetur adipiscing elit, sed do eiusmod tempor incididunt ut labore et dolore magna aliqua. Ut enim ad minim veniam, quis nostrud exercitation ullamco laboris nisi ut aliquip ex ea commodo consequat. Duis aute irure dolor in reprehenderit in voluptate velit esse cillum dolore eu fugiat nulla pariatur. Excepteur sint occaecat cupidatat non proident, sunt in culpa qui officia deserunt mollit anim id est laborum</p>
    </article>
    <article class="service">
      <svg class="service__icon" viewBox="0 0 70 70" fill="none" stroke="#b8822e" stroke-width="2.5"><rect x="8" y="12" width="54" height="42"/><path d="M8 20h54M16 28h14v10H16zM36 28h10M36 34h16M16 44h22"/><path d="M44 50l16-4"/></svg>
      <h3 class="service__title">BUILDING PLANNING EFFICIENCY SERVICES</h3>
      <p class="service__text">Lorem ipsum dolor sit amet, consectetur adipiscing elit, sed do eiusmod tempor incididunt ut labore et dolore magna aliqua. Ut enim ad minim veniam, quis nostrud exercitation ullamco laboris nisi ut aliquip ex ea commodo consequat. Duis aute irure dolor in reprehenderit in voluptate velit esse cillum dolore eu fugiat nulla pariatur. Excepteur sint occaecat cupidatat non proident, sunt in culpa qui officia deserunt mollit anim id est laborum</p>
    </article>
    <article class="service">
      <svg class="service__icon" viewBox="0 0 70 70" fill="none" stroke="#b8822e" stroke-width="2.5"><path d="M14 30l21-16 21 16M18 28v30h34V28"/><text x="27" y="50" text-anchor="middle" font-size="14" font-weight="700" fill="#b8822e" stroke="none" font-family="Mulish, sans-serif">$</text><rect x="36" y="38" width="10" height="10"/></svg>
      <h3 class="service__title">CONSTRUCTION COST REDUCTION SOLUTIONS</h3>
      <p class="service__text">Lorem ipsum dolor sit amet, consectetur adipiscing elit, sed do eiusmod tempor incididunt ut labore et dolore magna aliqua. Ut enim ad minim veniam, quis nostrud exercitation ullamco laboris nisi ut aliquip ex ea commodo consequat. Duis aute irure dolor in reprehenderit in voluptate velit esse cillum dolore eu fugiat nulla pariatur. Excepteur sint occaecat cupidatat non proident, sunt in culpa qui officia deserunt mollit anim id est laborum</p>
    </article>
    <article class="service" style="padding-top:22px">
      <svg class="service__icon" viewBox="0 0 70 70" fill="none" stroke="#b8822e" stroke-width="2.5" style="width:52px;height:52px"><rect x="14" y="8" width="36" height="46"/><path d="M20 58h36V14M32 16l8 6v8H24v-8zM22 38h20M22 44h20"/></svg>
      <h3 class="service__title">BUILDER'S PLANNING OPTIMIZATION CONSULTANCY</h3>
      <p class="service__text">Lorem ipsum dolor sit amet, consectetur adipiscing elit, sed do eiusmod tempor incididunt ut labore et dolore magna aliqua. Ut enim ad minim veniam, quis nostrud exercitation ullamco laboris nisi ut aliquip ex ea commodo consequat. Duis aute irure dolor in reprehenderit in voluptate velit esse cillum dolore eu fugiat nulla pariatur. Excepteur sint occaecat cupidatat non proident, sunt in culpa qui officia deserunt mollit anim id est laborum</p>
    </article>
  </div>
</section>

<section class="slide slide--team">
  <div class="brand"><span class="brand__square"></span>LUMO STACK</div>
  <h2 class="slide-title">OUR TEAM</h2>
  <div class="team">
    <article class="member">
      <div class="member__photo" role="img" aria-label="Portrait photo of a team member" style="background:linear-gradient(180deg,#f3c9a6,#e6b08a)"></div>
      <h3 class="member__name">MARTIN</h3>
      <p class="member__text">Lorem ipsum dolor sit amet, consectetur adipiscing elit, sed do eiusmod tempor incididunt ut labore et dolore magna aliqua. Ut enim ad minim veniam, quis nostrud exercitation ullamco laboris nisi ut aliquip ex ea commodo consequat.</p>
    </article>
    <article class="member">
      <div class="member__photo" role="img" aria-label="Portrait photo of a team member" style="background:linear-gradient(180deg,#6f7476,#535a5e)"></div>
      <h3 class="member__name">MARTIN</h3>
      <p class="member__text">Lorem ipsum dolor sit amet, consectetur adipiscing elit, sed do eiusmod tempor incididunt ut labore et dolore magna aliqua. Ut enim ad minim veniam, quis nostrud exercitation ullamco laboris nisi ut aliquip ex ea commodo consequat.</p>
    </article>
    <article class="member">
      <div class="member__photo" role="img" aria-label="Portrait photo of a team member" style="background:linear-gradient(180deg,#b7c3cc,#98a6b2)"></div>
      <h3 class="member__name">MARTIN</h3>
      <p class="member__text">Lorem ipsum dolor sit amet, consectetur adipiscing elit, sed do eiusmod tempor incididunt ut labore et dolore magna aliqua. Ut enim ad minim veniam, quis nostrud exercitation ullamco laboris nisi ut aliquip ex ea commodo consequat.</p>
    </article>
    <article class="member">
      <div class="member__photo" role="img" aria-label="Portrait photo of a team member" style="background:linear-gradient(180deg,#a9aaa6,#5f6f86)"></div>
      <h3 class="member__name">MARTIN</h3>
      <p class="member__text">Lorem ipsum dolor sit amet, consectetur adipiscing elit, sed do eiusmod tempor incididunt ut labore et dolore magna aliqua. Ut enim ad minim veniam, quis nostrud exercitation ullamco laboris nisi ut aliquip ex ea commodo consequat.</p>
    </article>
  </div>
</section>

<section class="slide slide--workflow">
  <div class="brand" style="top:22px"><span class="brand__square"></span>LUMO STACK</div>
  <h2 class="slide-title" style="top:28px">CAPACITIES AND PRESENT WORKFLOWS</h2>
  <div class="timeline-line"></div>
  <div class="step step--up" style="left:278px">
    <h3 class="step__title">LOREM IPSUM</h3>
    <p class="step__text">Lorem ipsum dolor sit amet, consectetur adipiscing elit, sed do eiusmod tempor incididunt ut labore et dolore magna aliqua. Ut enim ad minim veniam, quis nostrud exercitation</p>
    <span class="step__tick"></span>
  </div>
  <div class="step step--up" style="left:636px">
    <h3 class="step__title">LOREM IPSUM</h3>
    <p class="step__text">Lorem ipsum dolor sit amet, consectetur adipiscing elit, sed do eiusmod tempor incididunt ut labore et dolore magna aliqua. Ut enim ad minim veniam, quis nostrud exercitation</p>
    <span class="step__tick"></span>
  </div>
  <div class="step step--down" style="left:126px">
    <span class="step__tick"></span>
    <h3 class="step__title">LOREM IPSUM</h3>
    <p class="step__text">Lorem ipsum dolor sit amet, consectetur adipiscing elit, sed do eiusmod tempor incididunt ut labore et dolore magna aliqua. Ut enim ad minim veniam, quis nostrud exercitation ullamco laboris nisi ut aliquip ex ea commodo consequat.</p>
  </div>
  <div class="step step--down" style="left:453px">
    <span class="step__tick"></span>
    <h3 class="step__title">LOREM IPSUM</h3>
    <p class="step__text">Lorem ipsum dolor sit amet, consectetur adipiscing elit, sed do eiusmod tempor incididunt ut labore et dolore magna aliqua. Ut enim ad minim veniam, quis nostrud exercitation ullamco laboris nisi ut aliquip ex ea commodo consequat.</p>
  </div>
  <div class="step step--down" style="left:880px">
    <span class="step__tick"></span>
    <h3 class="step__title">LOREM IPSUM</h3>
    <p class="step__text">Lorem ipsum dolor sit amet, consectetur adipiscing elit, sed do eiusmod tempor incididunt ut labore et dolore magna aliqua. Ut enim ad minim veniam, quis nostrud exercitation ullamco laboris nisi ut aliquip ex ea commodo consequat.</p>
  </div>
</section>

<section class="slide slide--pricing">
  <div class="brand"><span class="brand__square"></span>LUMO STACK</div>
  <h2 class="slide-title">PRICING</h2>
  <div class="plans">
    <article class="plan">
      <header class="plan__head"><div class="plan__name">LOREM IPSUM</div><div class="plan__price">$26.00</div></header>
      <ul class="plan__list"><li>Lorem ipsum dolor sit amet</li><li>consectetur adipiscing elit, sed do</li><li>eiusmod tempor incididunt ut labore</li><li>et dolore magna aliqua. Ut enim ad</li><li>minim veniam, quis nostrud exercitation</li><li>ullamco laboris nisi ut aliquip ex ea</li><li>commodo consequat.</li><li>consectetur adipiscing elit, sed do</li><li>eiusmod tempor incididunt ut labore</li><li>commodo consequat.</li></ul>
    </article>
    <article class="plan">
      <header class="plan__head"><div class="plan__name">LOREM IPSUM</div><div class="plan__price">$26.00</div></header>
      <ul class="plan__list"><li>Lorem ipsum dolor sit amet</li><li>consectetur adipiscing elit, sed do</li><li>eiusmod tempor incididunt ut labore</li><li>et dolore magna aliqua. Ut enim ad</li><li>minim veniam, quis nostrud exercitation</li><li>ullamco laboris nisi ut aliquip ex ea</li><li>commodo consequat.</li><li>consectetur adipiscing elit, sed do</li><li>eiusmod tempor incididunt ut labore</li><li>commodo consequat.</li></ul>
    </article>
    <article class="plan">
      <header class="plan__head"><div class="plan__name">LOREM IPSUM</div><div class="plan__price">$26.00</div></header>
      <ul class="plan__list"><li>Lorem ipsum dolor sit amet</li><li>consectetur adipiscing elit, sed do</li><li>eiusmod tempor incididunt ut labore</li><li>et dolore magna aliqua. Ut enim ad</li><li>minim veniam, quis nostrud exercitation</li><li>ullamco laboris nisi ut aliquip ex ea</li><li>commodo consequat.</li><li>consectetur adipiscing elit, sed do</li><li>eiusmod tempor incididunt ut labore</li><li>commodo consequat.</li></ul>
    </article>
  </div>
</section>

<section class="slide slide--organization">
  <div class="brand"><span class="brand__square"></span>LUMO STACK</div>
  <h2 class="slide-title">ORGANIZATION</h2>
  <h3 class="org-heading">LOREM IPSUM DOLOR SIT AMET, CONSECTETUR ADIPISCING ELIT</h3>
  <p class="org-sub">Sed ut perspiciatis unde omnis iste natus error sit voluptatem</p>
  <svg class="chart" width="1002" height="562" viewBox="0 0 1002 562">
    <g stroke="var(--grid)" stroke-width="1">
      <line x1="50" x2="971" y1="195" y2="195"/><line x1="50" x2="971" y1="226" y2="226"/><line x1="50" x2="971" y1="258" y2="258"/><line x1="50" x2="971" y1="289" y2="289"/><line x1="50" x2="971" y1="320" y2="320"/><line x1="50" x2="971" y1="352" y2="352"/><line x1="50" x2="971" y1="383" y2="383"/><line x1="50" x2="971" y1="414" y2="414"/><line x1="50" x2="971" y1="445" y2="445"/><line x1="50" x2="971" y1="477" y2="477"/><line x1="50" x2="971" y1="508" y2="508"/>
      <line x1="50" x2="50" y1="195" y2="508"/><line x1="127" x2="127" y1="195" y2="508"/><line x1="204" x2="204" y1="195" y2="508"/><line x1="280" x2="280" y1="195" y2="508"/><line x1="357" x2="357" y1="195" y2="508"/><line x1="434" x2="434" y1="195" y2="508"/><line x1="511" x2="511" y1="195" y2="508"/><line x1="587" x2="587" y1="195" y2="508"/><line x1="664" x2="664" y1="195" y2="508"/><line x1="741" x2="741" y1="195" y2="508"/><line x1="818" x2="818" y1="195" y2="508"/><line x1="894" x2="894" y1="195" y2="508"/><line x1="971" x2="971" y1="195" y2="508"/>
    </g>
    <g text-anchor="end">
      <text x="44" y="198">100</text><text x="44" y="229">90</text><text x="44" y="261">80</text><text x="44" y="292">70</text><text x="44" y="323">60</text><text x="44" y="355">50</text><text x="44" y="386">40</text><text x="44" y="417">30</text><text x="44" y="448">20</text><text x="44" y="480">10</text><text x="44" y="511">0</text>
    </g>
    <g text-anchor="middle">
      <text x="88" y="532">JAN</text><text x="165" y="532">FEB</text><text x="242" y="532">MAR</text><text x="319" y="532">APR</text><text x="395" y="532">MAY</text><text x="472" y="532">JUN</text><text x="549" y="532">JUL</text><text x="626" y="532">AUG</text><text x="702" y="532">SEP</text><text x="779" y="532">OCT</text><text x="856" y="532">NOV</text><text x="933" y="532">DEC</text>
    </g>
    <polyline fill="none" stroke="var(--green)" stroke-width="1" points="50,383 127,352 204,383 280,289 357,289 434,320 511,289 587,289 664,236 741,226 818,226 894,236 971,226"/>
    <g fill="var(--green)">
      <circle cx="50" cy="383" r="4"/><circle cx="127" cy="352" r="4"/><circle cx="204" cy="383" r="4"/><circle cx="280" cy="289" r="4"/><circle cx="357" cy="289" r="4"/><circle cx="434" cy="320" r="4"/><circle cx="511" cy="289" r="4"/><circle cx="587" cy="289" r="4"/><circle cx="664" cy="236" r="4"/><circle cx="741" cy="226" r="4"/><circle cx="818" cy="226" r="4"/><circle cx="894" cy="236" r="4"/><circle cx="971" cy="226" r="4"/>
    </g>
    <polyline fill="none" stroke="var(--pink)" stroke-width="1" points="50,477 127,414 204,445 280,352 357,320 434,383 511,352 587,383 741,258 894,320 971,258"/>
    <g fill="var(--pink)">
      <circle cx="50" cy="477" r="4"/><circle cx="127" cy="414" r="4"/><circle cx="204" cy="445" r="4"/><circle cx="280" cy="352" r="4"/><circle cx="357" cy="320" r="4"/><circle cx="434" cy="383" r="4"/><circle cx="511" cy="352" r="4"/><circle cx="587" cy="383" r="4"/><circle cx="741" cy="258" r="4"/><circle cx="894" cy="320" r="4"/><circle cx="971" cy="258" r="4"/>
    </g>
  </svg>
</section>

</body>
</html>
```